Pegan Pyramid

Need a graphic for community lecture next week on preventing Cognitive Decline. Would like a Food Pyramid very similar to the one at this link, but with some adjustments:
1. Picture of "non-startchy veggie plant foods" might also include purple onion, garlic, purple cabbage, shitake mushrooms (in addition to what's pictured)
2. "Protein & Healthy Fats" would say "Mindful Protein & Healthy Fats". Picture should also include olive oil
3. Picture of starchy veggies would be more carrot/yam/beets/squash
http://www.tovashlend.com/wellness/grain-free-greens-the-plan-nobody-told-you-about/
Look forward to your design!!

```html
<!DOCTYPE html>
<html lang="en">
<head>
<meta charset="utf-8">
<title>Pegan Food Pyramid</title>
<link href="https://fonts.googleapis.com/css2?family=Open+Sans:wght@600;700;800&display=swap" rel="stylesheet">
<style>
  :root {
    --bg: #ffffff;
    --title: #5f5f5f;
    --subtitle: #8a55a6;
    --dot-a: #f3d6ec;
    --dot-b: #d9c8ef;
    --treat-a: #c45cc0;
    --treat-b: #7a3fbd;
    --treat-tag: #9a4cc0;
    --spice-a: #10d4d6;
    --spice-b: #24a0a6;
    --spice-tag: #178f8a;
    --bean-a: #f25ad2;
    --bean-b: #e0157f;
    --bean-tag: #e04ccb;
    --fruit-a: #1fc3f2;
    --fruit-b: #4a3cb0;
    --fruit-tag: #2d9ae0;
    --protein-a: #ffab1a;
    --protein-b: #e0601a;
    --veg-a: #8fd02a;
    --veg-b: #0e7f45;
    --text: #ffffff;
  }
  html, body { margin: 0; padding: 0; overflow: hidden; background: var(--bg); }
  .canvas { width: 1123px; height: 1200px; position: relative; overflow: hidden; }
  .canvas svg { display: block; width: 1123px; height: 1200px; }
  .title { font-family: "Open Sans", Arial, sans-serif; font-weight: 800; fill: var(--title); font-size: 68px; letter-spacing: 1px; }
  .subtitle { font-family: "Open Sans", Arial, sans-serif; font-weight: 700; fill: var(--subtitle); font-size: 25px; }
  .band-text { font-family: "Open Sans", Arial, sans-serif; font-weight: 700; fill: var(--text); text-anchor: middle; }
  .tag-text { font-family: "Open Sans", Arial, sans-serif; font-weight: 700; fill: var(--text); text-anchor: middle; }
  .dot { opacity: .7; }
</style>
</head>
<body>
<div class="canvas">
<svg viewBox="0 0 1000 1080" preserveAspectRatio="none" xmlns="http://www.w3.org/2000/svg">
  <defs>
    <linearGradient id="dot" x1="0" y1="0" x2="1" y2="1"><stop offset="0" stop-color="var(--dot-a)"/><stop offset="1" stop-color="var(--dot-b)"/></linearGradient>
    <linearGradient id="g-treat" x1="0" x2="1"><stop offset="0" stop-color="var(--treat-a)"/><stop offset="1" stop-color="var(--treat-b)"/></linearGradient>
    <linearGradient id="g-spice" x1="0" x2="1"><stop offset="0" stop-color="var(--spice-a)"/><stop offset="1" stop-color="var(--spice-b)"/></linearGradient>
    <linearGradient id="g-bean" x1="0" x2="1"><stop offset="0" stop-color="var(--bean-a)"/><stop offset="1" stop-color="var(--bean-b)"/></linearGradient>
    <linearGradient id="g-fruit" x1="0" x2="1"><stop offset="0" stop-color="var(--fruit-a)"/><stop offset="1" stop-color="var(--fruit-b)"/></linearGradient>
    <linearGradient id="g-protein" x1="0" x2="1"><stop offset="0" stop-color="var(--protein-a)"/><stop offset="1" stop-color="var(--protein-b)"/></linearGradient>
    <linearGradient id="g-veg" x1="0" x2="1"><stop offset="0" stop-color="var(--veg-a)"/><stop offset="1" stop-color="var(--veg-b)"/></linearGradient>
    <linearGradient id="p-treat" x1="0" y1="0" x2="1" y2="1"><stop offset="0" stop-color="#e9d2b0"/><stop offset="1" stop-color="#6b3b2a"/></linearGradient>
    <linearGradient id="p-spice" x1="0" y1="0" x2="1" y2="1"><stop offset="0" stop-color="#d9a13a"/><stop offset=".5" stop-color="#7a8a3a"/><stop offset="1" stop-color="#c23a2a"/></linearGradient>
    <linearGradient id="p-bean" x1="0" y1="0" x2="1" y2="1"><stop offset="0" stop-color="#8a4a32"/><stop offset=".5" stop-color="#d9c9b0"/><stop offset="1" stop-color="#b0572c"/></linearGradient>
    <linearGradient id="p-fruit" x1="0" y1="0" x2="1" y2="1"><stop offset="0" stop-color="#f0b23a"/><stop offset=".5" stop-color="#d9343a"/><stop offset="1" stop-color="#8fc23a"/></linearGradient>
    <linearGradient id="p-starch" x1="0" y1="0" x2="1" y2="1"><stop offset="0" stop-color="#e8781e"/><stop offset=".6" stop-color="#c0603a"/><stop offset="1" stop-color="#7a2a4a"/></linearGradient>
    <linearGradient id="p-protein" x1="0" y1="0" x2="1" y2="1"><stop offset="0" stop-color="#f0d2b0"/><stop offset=".5" stop-color="#a8302a"/><stop offset="1" stop-color="#d9b04a"/></linearGradient>
    <linearGradient id="p-veg" x1="0" y1="0" x2="1" y2="1"><stop offset="0" stop-color="#5a9a3a"/><stop offset=".6" stop-color="#3a7a2a"/><stop offset="1" stop-color="#7a3a7a"/></linearGradient>
  </defs>

  <g class="dots" fill="url(#dot)">
    <circle class="dot" cx="243" cy="195" r="45"/>
    <circle class="dot" cx="905" cy="195" r="45"/>
    <circle class="dot" cx="95" cy="300" r="45"/>
    <circle class="dot" cx="243" cy="378" r="45"/>
    <circle class="dot" cx="95" cy="462" r="45"/>
    <circle class="dot" cx="243" cy="545" r="45"/>
    <circle class="dot" cx="95" cy="640" r="45"/>
    <circle class="dot" cx="95" cy="810" r="45"/>
    <circle class="dot" cx="95" cy="1030" r="45"/>
    <circle class="dot" cx="420" cy="1030" r="45"/>
    <circle class="dot" cx="740" cy="1020" r="45"/>
  </g>

  <text class="title" x="500" y="95" text-anchor="middle">PEGAN FOOD PYRAMID</text>
  <text class="subtitle" x="500" y="140" text-anchor="middle">(adapted from Dr. Lena Marsh)</text>

  <!-- Tier 1: treats -->
  <g class="tier tier-treats">
    <polygon points="400,192 970,192 970,320 455,320 405,255" fill="url(#g-treat)"/>
    <polygon points="378,205 440,205 450,305 318,305" fill="url(#p-treat)" role="img" aria-label="Photo of wine, cupcake and chocolate"/>
    <polygon points="325,305 445,305 455,336 315,336" fill="var(--treat-tag)"/>
    <text class="tag-text" x="378" y="318" font-size="10">RECREATIONAL</text>
    <text class="tag-text" x="378" y="331" font-size="10">TREATS</text>
    <text class="band-text" x="727" y="271" font-size="23">SPARINGLY</text>
  </g>

  <!-- Tier 2: spices -->
  <g class="tier tier-spices">
    <polygon points="460,338 970,338 970,447 510,447 465,395" fill="url(#g-spice)"/>
    <polygon points="305,350 375,350 375,465 262,465" fill="url(#p-spice)" role="img" aria-label="Photo of spices and herbs in spoons"/>
    <polygon points="375,350 460,350 495,465 375,465" fill="var(--spice-tag)"/>
    <text class="tag-text" x="428" y="390" font-size="14">SPICES</text>
    <text class="tag-text" x="428" y="411" font-size="14">AND</text>
    <text class="tag-text" x="428" y="432" font-size="14">HERBS</text>
    <text class="band-text" x="733" y="385" font-size="22">UNLIMITED</text>
    <text class="band-text" x="733" y="414" font-size="22">AMOUNTS</text>
  </g>

  <!-- Tier 3: beans -->
  <g class="tier tier-beans">
    <polygon points="505,465 970,465 970,583 550,583 505,525" fill="url(#g-bean)"/>
    <polygon points="255,482 360,482 360,600 205,600" fill="url(#p-bean)" role="img" aria-label="Photo of bowls of beans, lentils and grains"/>
    <polygon points="360,482 505,482 550,600 360,600" fill="var(--bean-tag)"/>
    <text class="tag-text" x="440" y="528" font-size="12.5">BEANS, LEGUMES,</text>
    <text class="tag-text" x="440" y="548" font-size="12.5">NON GLUTEN</text>
    <text class="tag-text" x="440" y="568" font-size="12.5">GRAINS</text>
    <text class="band-text" x="752" y="504" font-size="18">INCLUDE UP TO 1/2</text>
    <text class="band-text" x="752" y="531" font-size="18">CUP OF GLUTEN FREE GRAINS, UP TO</text>
    <text class="band-text" x="752" y="558" font-size="18">1/2 CUP OF BEANS</text>
  </g>

  <!-- Tier 4: fruits & starchy veggies -->
  <g class="tier tier-fruits">
    <polygon points="580,602 970,602 970,718 625,718 580,660" fill="url(#g-fruit)"/>
    <polygon points="200,615 360,615 360,705 165,705" fill="url(#p-fruit)" role="img" aria-label="Photo of mixed fresh fruit"/>
    <polygon points="400,615 570,615 612,705 400,705" fill="url(#p-starch)" role="img" aria-label="Photo of squash, carrots, beets and yams"/>
    <polygon points="150,708 385,708 375,735 140,735" fill="var(--fruit-tag)"/>
    <polygon points="400,708 612,708 625,735 400,735" fill="#2a6fd0"/>
    <text class="tag-text" x="262" y="730" font-size="19">FRUITS</text>
    <text class="tag-text" x="505" y="730" font-size="19">STARCHY VEGGIES</text>
    <text class="band-text" x="788" y="641" font-size="14">FOCUS ON LOW GLYCEMIC FRUIT</text>
    <text class="band-text" x="788" y="663" font-size="14">(1 CUP PER DAY) &amp; UP TO 2 SERVINGS</text>
    <text class="band-text" x="788" y="685" font-size="14">OF STARCHY VEGGIES PER DAY</text>
  </g>

  <!-- Tier 5: protein & fats -->
  <g class="tier tier-protein">
    <polygon points="625,735 970,735 970,850 670,850 625,790" fill="url(#g-protein)"/>
    <polygon points="140,750 345,750 345,868 92,868" fill="url(#p-protein)" role="img" aria-label="Photo of eggs, salmon, meat, avocado, quinoa and olive oil"/>
    <polygon points="345,750 625,750 670,868 345,868" fill="var(--protein-a)"/>
    <text class="tag-text" x="495" y="806" font-size="20">MINDFUL PROTEIN &amp;</text>
    <text class="tag-text" x="495" y="835" font-size="20">HEALTHY FATS</text>
    <text class="band-text" x="795" y="772" font-size="18">4-6 OZ OF PROTEIN PER</text>
    <text class="band-text" x="795" y="799" font-size="18">MEAL, &amp; 3-5 SERVINGS OF</text>
    <text class="band-text" x="795" y="826" font-size="18">FAT PER DAY</text>
  </g>

  <!-- Tier 6: non-starchy veggies -->
  <g class="tier tier-veg">
    <polygon points="700,868 970,868 970,985 740,985 700,925" fill="url(#g-veg)"/>
    <polygon points="95,885 265,885 265,1010 48,1010" fill="url(#p-veg)" role="img" aria-label="Photo of broccoli, greens, purple cabbage, onion, garlic and mushrooms"/>
    <polygon points="265,885 700,885 740,1010 265,1010" fill="url(#g-veg)"/>
    <text class="tag-text" x="498" y="940" font-size="27">NON STARCHY VEGGIE</text>
    <text class="tag-text" x="498" y="976" font-size="27">PLANT FOODS</text>
    <text class="band-text" x="853" y="919" font-size="21">UNLIMITED</text>
    <text class="band-text" x="853" y="948" font-size="21">AMOUNTS</text>
  </g>
</svg>
</div>
</body>
</html>
```